Tarvick homes and renovations business card design.

Would like some new card designs utilizing my new logo that look professional. I am open to different colors on the logo or utilize the same ones we have. I like the original concept but would like to see some fresh ideas and build on what we have already done.

Target Market(s)

Custom home building industry, Real estate sales, Renovation projects.

Industry/Entity Type

Home Builder

Contact Information for Business Card

Tarvick Homes and Renovations
2871 92nd Avenue
Merrowdale, Westmark
R3J2W5
Home : 403- 718-4305 Cell: 403- 294-1537

My info is : Dax Tarvick, President and CEO
email: tarvickhomes@quillpost.net
Website: tarvickhomes.net

Requirements
Must have
• Must Use my new logo design. I am open to different colors on the logo or utilize the same ones in the existing design. I can upload the original logo design if needed.

```html
<!DOCTYPE html>
<html lang="en">
<head>
<meta charset="utf-8">
<title>Tarvick Homes and Renovations – Business Card</title>
<link href="https://fonts.googleapis.com/css2?family=Open+Sans:wght@400;600;700&display=swap" rel="stylesheet">
<style>
  :root {
    --backdrop: #e7e7e7;
    --card-white: #fbfbfb;
    --brand-yellow: #f3b922;
    --brand-gold: #b5893a;
    --white: #ffffff;
  }
  html, body {
    margin: 0;
    width: 1200px;
    height: 900px;
    overflow: hidden;
    background: var(--backdrop);
    font-family: "Open Sans", Arial, sans-serif;
  }
  .canvas {
    position: relative;
    width: 1200px;
    height: 900px;
  }
  .card {
    position: absolute;
    top: 313px;
    width: 490px;
    height: 280px;
    box-sizing: border-box;
    box-shadow: 0 6px 18px rgba(0,0,0,0.12);
  }
  .card--front { left: 90px; background: var(--card-white); padding: 30px 32px; }
  .card--back  { left: 620px; background: var(--brand-yellow); display: flex; align-items: center; justify-content: center; }

  .holder-name {
    margin: 0;
    font-size: 17px;
    font-weight: 700;
    letter-spacing: 0.5px;
    text-transform: uppercase;
    color: var(--brand-yellow);
  }
  .holder-title {
    margin: 2px 0 0;
    font-size: 11px;
    color: var(--brand-gold);
  }

  .wordmark {
    margin: 0;
    font-weight: 700;
    line-height: 1.1;
  }
  .wordmark--front {
    position: absolute;
    left: 32px;
    top: 118px;
    width: 190px;
    font-size: 19px;
    color: var(--brand-gold);
  }
  .wordmark--back {
    width: 300px;
    font-size: 28px;
    text-align: center;
    color: var(--white);
  }

  .contact-list {
    position: absolute;
    right: 32px;
    top: 96px;
    margin: 0;
    padding: 0;
    list-style: none;
    text-align: right;
    font-size: 11px;
    line-height: 17px;
    color: var(--brand-gold);
  }
  .contact-list li { display: flex; justify-content: flex-end; align-items: center; gap: 6px; }
  .contact-list svg { width: 10px; height: 10px; fill: var(--brand-yellow); }

  .address {
    position: absolute;
    right: 32px;
    bottom: 30px;
    margin: 0;
    text-align: right;
    font-style: normal;
    font-size: 11px;
    line-height: 16px;
    color: var(--brand-gold);
  }
  .address__company { font-weight: 700; color: var(--brand-yellow); }
</style>
</head>
<body>
<main class="canvas">
  <section class="card card--front" aria-label="Business card front">
    <h1 class="holder-name">Dax Tarvick</h1>
    <p class="holder-title">President and CEO</p>

    <p class="wordmark wordmark--front">Tarvick Homes and Renovations</p>

    <ul class="contact-list">
      <li>403- 718-4305
        <svg viewBox="0 0 10 10"><path d="M2 0h2l1 3-1.5 1a6 6 0 0 0 2.5 2.5L7 5l3 1v2a2 2 0 0 1-2 2A8 8 0 0 1 0 2a2 2 0 0 1 2-2z"/></svg></li>
      <li>403- 294-1537
        <svg viewBox="0 0 10 10"><path d="M2.5 0h5v10h-5zM3.5 1v7h3V1z" fill-rule="evenodd"/></svg></li>
      <li>tarvickhomes@quillpost.net
        <svg viewBox="0 0 10 10"><path d="M0 2h10v6H0zM0.8 2.6 5 5.6l4.2-3z" fill-rule="evenodd"/></svg></li>
      <li>www.tarvickhomes.net
        <svg viewBox="0 0 10 10"><circle cx="5" cy="5" r="5"/></svg></li>
    </ul>

    <address class="address">
      <span class="address__company">Tarvick homes and Renovations</span><br>
      2871 92nd Avenue<br>
      Merrowdale, Westmark R3J2W5
    </address>
  </section>

  <section class="card card--back" aria-label="Business card back">
    <p class="wordmark wordmark--back">Tarvick Homes and Renovations</p>
  </section>
</main>
</body>
</html>
```